Start up in business consultancy needs a business card

We need the business card's layout (we have already the logo). Our business is concerned on consultancy services delivered to companies on the matter of sustainability. Business card should be enough essentials and professional style.

Side A with the following info:
logo + a space for the claim (still to identify) + website of the company

Side B with the following info:
Name of business card holder + title of the business card holder + address of the company + space for mobile number, phone number, fax number + e-mail of business card holder + graphic details around.

Target Market(s)

Business of any sector

Industry/Entity Type

Business Service

Contact Information for Business Card

Name of the company:
Lumeroca srl
Società Benefit

Address of the company:
Via Pescoli, 7
21099 - Gallarate (VA)

Website:
www.lumeroca-esempio.it

Name of the BC' holder:
Ettore Valsenzi

Title:
Co-fondatore

Email:
ettore@lumeroca-esempio.it

Mobile:
+39 351 602 7415
Phone:
+39 351 602 7415
Fax:
+39 351 602 7415

Font styles to use
Other font styles liked:
• new gothic

```html
<!DOCTYPE html>
<html lang="it">
<head>
<meta charset="utf-8">
<title>Lumeroca – Biglietto da visita</title>
<link href="https://fonts.googleapis.com/css2?family=News+Cycle:wght@400;700&display=swap" rel="stylesheet">
<style>
  :root {
    --brand-blue: #1668ad;
    --paper: #ffffff;
    --ink: #3a3a3a;
    --backdrop: #2e2019;
  }
  * { margin: 0; padding: 0; box-sizing: border-box; }
  html, body {
    width: 1200px; height: 1000px; overflow: hidden;
    background: var(--backdrop);
    font-family: "News Cycle", "Arial Narrow", sans-serif;
  }
  .canvas { position: relative; width: 1200px; height: 1000px; }

  .card {
    position: absolute;
    background: var(--paper);
    box-shadow: 0 6px 18px rgba(0,0,0,.45);
    overflow: hidden;
  }

  /* Side B – holder details */
  .card--details { left: 170px; top: 190px; width: 600px; height: 330px; }
  .brand-panel {
    position: absolute; left: 0; top: 0; bottom: 0; width: 235px;
    background: var(--brand-blue); color: var(--paper);
  }
  .brand-panel__name {
    position: absolute; left: 22px; top: 160px;
    font-size: 44px; font-weight: 700; letter-spacing: .5px;
  }
  .brand-panel__legal {
    position: absolute; right: 18px; bottom: 28px;
    font-size: 17px; line-height: 1.05; text-align: right;
  }
  .holder { position: absolute; left: 268px; top: 62px; color: var(--ink); }
  .holder__name {
    font-size: 23px; font-weight: 700; color: var(--brand-blue);
    text-transform: uppercase; letter-spacing: .3px; line-height: 1;
  }
  .holder__title { font-size: 17px; margin-top: 2px; }
  .contact-list { list-style: none; margin-top: 16px; font-size: 16px; line-height: 20px; }
  .contact-list li { display: flex; align-items: center; gap: 8px; }
  .contact-list .gap { margin-top: 10px; }
  .contact-list .indent { padding-left: 22px; }
  .icon { width: 14px; height: 14px; flex: none; fill: var(--brand-blue); }

  /* Side A – brand and website */
  .card--brand { left: 480px; top: 540px; width: 526px; height: 300px; }
  .brand-name {
    position: absolute; left: 24px; top: 228px;
    font-size: 28px; font-weight: 700; color: var(--brand-blue);
    line-height: 40px;
  }
  .web-band {
    position: absolute; left: 284px; right: 0; top: 230px; height: 34px;
    background: var(--brand-blue); color: var(--paper);
    font-size: 19px; line-height: 34px; padding-left: 36px;
  }
</style>
</head>
<body>
<main class="canvas">

  <section class="card card--details">
    <div class="brand-panel">
      <div class="brand-panel__name">Lumeroca</div>
      <div class="brand-panel__legal">srl Società<br>Benefit</div>
    </div>
    <div class="holder">
      <h1 class="holder__name">Ettore Valsenzi</h1>
      <p class="holder__title">Co-fondatore</p>
      <ul class="contact-list">
        <li><svg class="icon" viewBox="0 0 14 14"><path d="M3 0h8v14H3z M4.5 1.5v10h5v-10z"/></svg>+39 351 602 7415</li>
        <li><svg class="icon" viewBox="0 0 14 14"><path d="M1 4c0-2 12-2 12 0v2h-3V4.5H4V6H1z M3 7h8l2 6H1z"/></svg>+39 351 602 7415</li>
        <li><svg class="icon" viewBox="0 0 14 14"><path d="M3 0h8v4H3z M0 5h14v6h-3v3H3v-3H0z M4 9v3h6V9z"/></svg>+39 351 602 7415</li>
        <li class="gap"><svg class="icon" viewBox="0 0 14 14"><path d="M0 3h14v1L7 8 0 4z M0 5.5l7 4 7-4V12H0z"/></svg>ettore@lumeroca-esempio.it</li>
        <li><svg class="icon" viewBox="0 0 14 14"><path d="M7 0a5 5 0 0 1 5 5c0 4-5 9-5 9S2 9 2 5a5 5 0 0 1 5-5z M7 3a2 2 0 1 0 0 4 2 2 0 0 0 0-4z"/></svg>Via Pescoli, 7 , 21099</li>
        <li class="indent">Corvenna (CV)</li>
      </ul>
    </div>
  </section>

  <section class="card card--brand">
    <div class="brand-name">Lumeroca</div>
    <div class="web-band">www.lumeroca-esempio.it</div>
  </section>

</main>
</body>
</html>
```